Flyer Design Project

I need a cool design that describes a new line of services I am selling. The final product should be a 8 1/2 by 11 and maximum two pages.

I am selling consulting services to learn to use web conferencing tools for business development, meeting and training.

Please use the file I have attached as a guide for your work. It is a document called "primer-thriftyhacksguide" and I love its design.

Thanks

                                        Please substitute the new text availble and just uploaded in the FLYER. Please submit the FINAL version fo your design with TExt changes as well as improvements detailed in previous message. 

Target Market(s)

Entrepreneurs and classroom educators who wnats to explore a new way to teach (innovators not scared of technology)

Industry/Entity Type

Business

Requirements
Must have
• I would like to receive a final PDF with the content EDITABLE for minor edits (I have acrobat)
Logo should be included (attached)

PLEASE CHECK OUT ATTACHED DOCUMENT WHOSE DESIGN I LOVE.
IT is called "Primer thrifty-hacks guide". If you could follow that as a template to design mine that would be great!

```html
<!DOCTYPE html>
<html lang="en">
<head>
<meta charset="utf-8">
<title>Online Meeting Skills Services – Flyer</title>
<link href="https://fonts.googleapis.com/css2?family=Arimo:ital,wght@0,400;0,700;1,400&display=swap" rel="stylesheet">
<style>
  :root {
    --backdrop: #e6e9ed;
    --paper: #ffffff;
    --brand-blue: #1f6fb6;
    --deep-blue: #174f8a;
    --band-light: #4b92d0;
    --ink: #222222;
    --muted: #555a60;
    --rule: #9fc1e3;
    --gold: #f3d766;
    --gold-soft: #fbf1c4;
    --photo-light: #c9dcf0;
    --photo-dark: #3d6f9f;
  }
  * { box-sizing: border-box; margin: 0; padding: 0; }
  html, body { width: 1200px; height: 900px; overflow: hidden; }
  body {
    background: var(--backdrop);
    font-family: "Arimo", Arial, sans-serif;
    color: var(--ink);
    display: flex;
    gap: 24px;
    padding: 212px 24px;
  }
  .page {
    width: 368px;
    height: 476px;
    background: var(--paper);
    box-shadow: 0 2px 8px rgba(0,0,0,.18);
    position: relative;
    overflow: hidden;
  }

  /* Brand name block */
  .brand { display: flex; align-items: center; gap: 6px; }
  .brand-mark { width: 9px; height: 9px; border-radius: 50%; background: var(--brand-blue); }
  .brand-name { font-weight: 700; color: var(--brand-blue); font-size: 17px; letter-spacing: .2px; }
  .brand-tagline { font-size: 7px; color: var(--muted); margin-top: 2px; }

  /* Cover */
  .cover-head { padding: 22px 0 0; display: flex; flex-direction: column; align-items: center; }
  .cover-photo {
    position: absolute; left: 28px; right: 0; top: 78px; height: 212px;
    background: linear-gradient(135deg, var(--photo-light) 0%, #8fb4da 45%, var(--photo-dark) 100%);
  }
  .cover-title { position: absolute; left: 28px; right: 18px; top: 316px; }
  .cover-title h1 { font-size: 27px; line-height: 1.08; color: var(--brand-blue); font-weight: 700; }
  .cover-title p { font-size: 23px; line-height: 1.15; margin-top: 6px; color: var(--ink); }

  /* Services page */
  .services { padding: 14px 22px; }
  .running-head {
    text-align: right; font-size: 8px; font-weight: 700; color: var(--deep-blue);
    letter-spacing: .6px; border-bottom: 1.5px solid var(--rule); padding-bottom: 4px; margin-bottom: 8px;
  }
  .services h2 { font-size: 10.5px; line-height: 1.2; color: var(--brand-blue); font-weight: 700; margin: 6px 0 4px; }
  .services p, .services li { font-size: 6.1px; line-height: 1.45; color: var(--ink); }
  .services p { margin-bottom: 3px; }
  .services ul { padding-left: 9px; margin-bottom: 3px; }
  .services li { margin-bottom: 2px; }

  /* Membership page */
  .membership-head { display: flex; justify-content: space-between; align-items: flex-start; padding: 16px 16px 8px; }
  .membership-head .brand-name { font-size: 13px; }
  .community-line { text-align: right; font-size: 8.5px; font-weight: 700; color: var(--deep-blue); line-height: 1.2; letter-spacing: .3px; }
  .benefits-band {
    background: linear-gradient(90deg, var(--band-light), var(--deep-blue));
    color: #fff; font-size: 8px; font-weight: 700; letter-spacing: .8px;
    padding: 5px 16px; text-align: center;
  }
  .benefits-body { display: flex; gap: 12px; padding: 12px 16px 12px; }
  .benefits-lead { flex: 1; font-size: 8.6px; line-height: 1.22; font-weight: 700; color: var(--brand-blue); }
  .benefits-text { flex: 1; font-size: 5.6px; line-height: 1.45; color: var(--ink); }
  .benefits-text p + p { margin-top: 5px; }

  .plan-table { width: calc(100% - 32px); margin: 0 16px; border-collapse: collapse; }
  .plan-table th {
    background: var(--gold); font-size: 5.6px; font-weight: 700; color: var(--ink);
    padding: 5px 2px; border: 1px solid #fff;
  }
  .plan-table th.blank { background: none; }
  .plan-table td { font-size: 5.2px; line-height: 1.4; vertical-align: top; padding: 6px 4px; height: 46px; border: 1px solid #fff; }
  .plan-table td.feature { width: 44%; padding-left: 0; border-top: 1px solid var(--rule); }
  .plan-table td.cell { background: var(--gold-soft); text-align: center; }
  .feature-title { display: block; font-weight: 700; color: var(--deep-blue); font-size: 5.4px; margin-bottom: 2px; }

  .contact-band {
    position: absolute; left: 0; right: 0; bottom: 0; height: 24px;
    background: linear-gradient(90deg, var(--band-light), var(--deep-blue));
    color: #fff; font-size: 7.5px; font-weight: 700; display: flex; align-items: center; justify-content: center;
  }
</style>
</head>
<body>

  <section class="page cover">
    <header class="cover-head">
      <div class="brand">
        <span class="brand-mark"></span>
        <span class="brand-name">Convene Consulting</span>
      </div>
      <div class="brand-tagline">Learn. Connect. Grow.</div>
    </header>
    <div class="cover-photo" role="img" aria-label="Photo of a piggy bank standing on a laptop keyboard in cool blue light"></div>
    <div class="cover-title">
      <h1>Online Meeting Skills Services</h1>
      <p>It is just the beginning…</p>
    </div>
  </section>

  <section class="page services">
    <div class="running-head">ONLINE MEETING SKILLS SERVICES</div>
    <h2>What if your business can reach all the people you want to reach in learning what you know?</h2>
    <p>A different way of webinar technology: the first step towards a new way to reach markets and grow your clients.</p>
    <p>You probably know about webinars. You have probably attended a few yourself. We help you plan, design and deliver engaging online sessions that turn attendees into loyal learners and buyers, without the cost of travel or rented rooms.</p>
    <ul>
      <li>We design an effective virtual meeting experience for you using the tools and formats that suit your goals, your audience and your budget.</li>
      <li>We produce your sessions, handle registration and follow-up, and give you clear reports on attendance, engagement and results.</li>
      <li>We coach your team to present with confidence and keep every audience engaged from start to finish, with polls, chat and breakouts.</li>
      <li>We help you record, edit and reuse each session so your content keeps working for you long after the live event ends.</li>
    </ul>
    <h2>Choose the service that best fit your needs and level of online engagement and virtual collaboration</h2>
    <ul>
      <li>“Webinar Starter” Plan, design and deliver a first live session with our guidance, step by step, from invitation to follow-up email.</li>
      <li>“Virtual Classroom” Build a short online course for your learners and run it with our support, including materials and activities.</li>
      <li>“Getting Online Confidence” A half-day hands-on workshop for presenters who are new to web tools and want to feel at ease.</li>
      <li>“Presenting for Online Audiences” Design and deliver polished sessions that keep people listening and ready to act.</li>
      <li>“One-on-One Coaching” Private sessions to review your slides, voice and pacing and to rehearse before a key event.</li>
    </ul>
    <h2>You’ll participate via the Linkwise Meeting platform. No special software is required. If you have a computer with Internet access and a direct telephone line you have all is needed to participate.</h2>
    <p>As a small business owner or educator you know that webinar technology is here to stay. Share your expertise, reach new markets and save the costs of travel by bringing your audience to you, wherever they are.</p>
  </section>

  <section class="page membership">
    <header class="membership-head">
      <div>
        <div class="brand">
          <span class="brand-mark"></span>
          <span class="brand-name">Convene Consulting</span>
        </div>
        <div class="brand-tagline">Learn. Connect. Grow.</div>
      </div>
      <div class="community-line">A WORLDWIDE COMMUNITY<br>FOR eLEARNING PROFESSIONALS</div>
    </header>
    <div class="benefits-band">THE BENEFITS OF MEMBERSHIP</div>
    <div class="benefits-body">
      <div class="benefits-lead">Lorem ipsum dolor sit amet, consectetuer adipiscing elit. Morbi commodo, ipsum sed pharetra gravida, orci magna rhoncus neque, id pulvinar odio lorem non turpis. Nullam sit amet enim. Suspendisse id velit vitae ligula volutpat condimentum. Aliquam erat volutpat. Sed quis velit. Nulla facilisi. Nulla libero. Vivamus pharetra posuere sapien. Nam consectetuer. Sed aliquam, nunc eget euismod ullamcorper, lectus nunc ullamcorper orci, fermentum bibendum enim aliquam.</div>
      <div class="benefits-text">
        <p>Lorem ipsum dolor sit amet, consectetuer adipiscing elit. Morbi commodo, ipsum sed pharetra gravida, orci magna rhoncus neque, id pulvinar odio lorem non turpis. Nullam sit amet enim sed velit ultrices. Suspendisse id velit vitae ligula volutpat condimentum. Aliquam erat volutpat. Sed quis velit. Nulla facilisi. Nulla libero.</p>
        <p>Sed aliquam, nunc eget euismod ullamcorper, lectus nunc ullamcorper orci, fermentum bibendum enim nibh eget ipsum. Donec porttitor ligula eu dolor. Maecenas vitae nulla consequat libero cursus venenatis. Nam magna enim, accumsan eu, blandit sed, blandit a, eros.</p>
        <p>Sed aliquam, nunc eget euismod ullamcorper, lectus nunc ullamcorper orci, fermentum bibendum enim nibh eget ipsum. Nulla facilisi.</p>
      </div>
    </div>
    <table class="plan-table">
      <thead>
        <tr><th class="blank"></th><th>MEMBER</th><th>PREMIUM MEMBER</th><th>PREMIUM MEMBER</th></tr>
      </thead>
      <tbody>
        <tr>
          <td class="feature"><span class="feature-title">ENTER TITLE HERE</span>Phasellus sagittis, nulla in hendrerit laoreet, libero lacus feugiat urna, eget phasellus pede magna laoreet.</td>
          <td class="cell">Phasellus sagittis, pede magna laor.</td>
          <td class="cell">Phasellus sagittis, pede magna laor.</td>
          <td class="cell">Phasellus sagittis, pede magna laor.</td>
        </tr>
        <tr>
          <td class="feature"><span class="feature-title">ENTER TITLE HERE</span>Phasellus sagittis, nulla in hendrerit laoreet, libero lacus feugiat urna, eget phasellus pede magna laoreet.</td>
          <td class="cell">Phasellus sagittis, pede magna laor.</td>
          <td class="cell">Phasellus sagittis, pede magna laor.</td>
          <td class="cell">Phasellus sagittis, pede magna laor.</td>
        </tr>
        <tr>
          <td class="feature"><span class="feature-title">ENTER TITLE HERE</span>Phasellus sagittis, nulla in hendrerit laoreet, libero lacus feugiat urna, eget phasellus pede magna laoreet.</td>
          <td class="cell">Phasellus sagittis, pede magna laor.</td>
          <td class="cell">Phasellus sagittis, pede magna laor.</td>
          <td class="cell">Phasellus sagittis, pede magna laor.</td>
        </tr>
      </tbody>
    </table>
    <footer class="contact-band">For more information, give us a call at 202-555-0187.</footer>
  </section>

</body>
</html>
```